Flyer for KW Alarm Technicians

This flyer will help our technicians upsell/educate our current customers on the different service packages that we offer when the tech is in the customers home.

```html
<!DOCTYPE html>
<html lang="en">
<head>
<meta charset="utf-8">
<title>KW Alarm Technicians – Packages</title>
<link rel="stylesheet" href="https://fonts.googleapis.com/css2?family=Montserrat:wght@400;500;700&display=swap">
<style>
  :root {
    --green: #14a23c;
    --green-dark: #0d8a2f;
    --blue: #1f5fae;
    --ink: #4a4a4a;
    --grey-text: #6a6a6a;
    --stage: #dcdcdc;
    --white: #ffffff;
  }
  * { margin: 0; padding: 0; box-sizing: border-box; }
  html, body { width: 872px; height: 1200px; overflow: hidden; background: var(--stage); }
  body { font-family: "Montserrat", sans-serif; color: var(--ink); position: relative; }

  .page { position: absolute; top: 301px; width: 683px; height: 963px; overflow: hidden;
    transform: scale(0.62); transform-origin: 0 0;
    background: linear-gradient(180deg, #fff 0, #fff 45%, #f1f1f1 100%); }
  .page-front { left: 8px; }
  .page-back { left: 441px; }

  .t { position: absolute; white-space: nowrap; line-height: 1; }
  .center { left: 0; width: 100%; text-align: center; }
  .bold { font-weight: 700; }
  .green { color: var(--green); }
  .blue { color: var(--blue); }
  .white { color: var(--white); }

  .photo { position: absolute; border-radius: 6px; }
  .rule { position: absolute; height: 2px; background: var(--green); }
  .rule::before { content: ""; position: absolute; left: -4px; top: -4px; width: 10px; height: 10px;
    border-radius: 50%; background: var(--green); }
  .footer-bar { position: absolute; bottom: 0; height: 17px; background: var(--green); }

  /* front */
  .brand-name { top: 64px; font-size: 34px; font-weight: 500; color: var(--blue); letter-spacing: 1px; }
  .brand-sub { top: 114px; font-size: 21px; color: var(--ink); letter-spacing: 17px; padding-left: 17px; }
  .offer-band { position: absolute; top: 189px; left: 0; }
  .offer-line { font-size: 21px; font-weight: 500; }
  .offer-line strong { font-size: 30px; font-weight: 700; }
  .hero-photo { left: 0; top: 320px; width: 316px; height: 643px; border-radius: 0;
    background: radial-gradient(circle at 52% 48%, #1e1e1e 0 24%, #d8d8d8 25%, #ececec 55%, #f4f4f4 100%); }
  .hero-label { left: 93px; top: 398px; font-size: 19px; font-weight: 500; color: var(--grey-text); }
  .hero-pointer { position: absolute; left: 181px; top: 420px; width: 2px; height: 77px; background: var(--green); }
  .hero-dot { position: absolute; left: 175px; top: 490px; width: 14px; height: 14px; border-radius: 50%; background: var(--green); }
  .device-photo { left: 376px; width: 130px; }
  .device-label { left: 518px; font-size: 14px; font-weight: 700; line-height: 17px; color: #555; }
  .device-rule { left: 494px; width: 119px; }

  /* back */
  .cam-photo { left: 0; top: 134px; width: 391px; height: 240px; border-radius: 0 60px 60px 0;
    background: linear-gradient(90deg, #bfbfbf 0, #ececec 45%, #f7f7f7 60%, #1a1a1a 75%, #2a2a2a 88%, #e6e6e6 100%); }
  .head-line { font-size: 21px; font-weight: 500; }
  .head-line strong { font-size: 30px; font-weight: 700; }
  .sec-lead { left: 68px; font-size: 16px; font-weight: 500; }
  .sec-bold { left: 69px; font-size: 18px; font-weight: 700; }
  .detail { left: 239px; font-size: 15px; color: var(--ink); }
  .fine { left: 239px; font-size: 8.5px; font-weight: 500; }
  .panel-line { left: 68px; font-size: 19px; }
</style>
</head>
<body>

<article class="page page-front">
  <div class="t center brand-name">KW ALARM TECHNICIANS</div>
  <div class="t center brand-sub">PACKAGES</div>

  <svg class="offer-band" width="683" height="144" viewBox="0 0 683 144">
    <path d="M0 0 H683 V144 H0 Z" fill="var(--green)"/>
    <path d="M0 144 V131 H616 Q626 131 630 144 Z" fill="#f7f7f7"/>
  </svg>
  <div class="t center white offer-line" style="top:212px">ONE HOME AUTOMATION DEVICE</div>
  <div class="t center white offer-line" style="top:240px">REQUIRES <strong>A $6 A MONTH INCREASE</strong></div>
  <div class="t center white offer-line" style="top:276px">PER DEVICE WITH A 60 MONTH RENEWAL</div>

  <div class="photo hero-photo" role="img" aria-label="Photo of a white and black indoor security camera"></div>
  <div class="t hero-label">INDOOR CAMERA</div>
  <div class="hero-pointer"></div>
  <div class="hero-dot"></div>

  <div class="photo device-photo" style="top:349px;height:110px;background:linear-gradient(135deg,#e6e6e6,#9a9a9a 55%,#1c1c1c)" role="img" aria-label="Photo of two doorbell cameras"></div>
  <div class="t device-label" style="top:385px">DOOR<br>BELL CAMERAS</div>
  <div class="rule device-rule" style="top:426px"></div>

  <div class="photo device-photo" style="top:514px;height:105px;background:linear-gradient(135deg,#fafafa,#dcdcdc)" role="img" aria-label="Photo of a white wall thermostat"></div>
  <div class="t device-label" style="top:545px">NTC<br>THERMOSTAT</div>
  <div class="rule device-rule" style="top:586px"></div>

  <div class="photo device-photo" style="top:672px;height:97px;background:linear-gradient(90deg,#cfcfcf,#d2b04a 50%,#2b2b2b)" role="img" aria-label="Photo of three keypad deadbolts in nickel, brass and bronze"></div>
  <div class="t device-label" style="top:699px">AUTO<br>DEADBOLT</div>
  <div class="rule device-rule" style="top:740px"></div>

  <div class="photo device-photo" style="top:822px;height:107px;background:linear-gradient(135deg,#3a3a3a,#111)" role="img" aria-label="Photo of a black garage door controller"></div>
  <div class="t device-label" style="top:854px">GARAGE<br>CONTROLLER</div>
  <div class="rule device-rule" style="top:895px"></div>

  <div class="footer-bar" style="left:316px;width:367px"></div>
</article>

<article class="page page-back">
  <svg style="position:absolute;left:0;top:0" width="683" height="262" viewBox="0 0 683 262">
    <defs>
      <linearGradient id="headGreen" x1="0" y1="0" x2="1" y2="1">
        <stop offset="0" stop-color="var(--green)"/>
        <stop offset="1" stop-color="var(--green-dark)"/>
      </linearGradient>
    </defs>
    <path d="M0 0 H683 V261 H0 Z" fill="url(#headGreen)"/>
    <path d="M380 262 V249 H616 Q624 249 628 262 Z" fill="#fff"/>
  </svg>
  <div class="t center white head-line" style="top:37px">OUTDOOR CAMERA</div>
  <div class="t center white head-line" style="top:64px">REQUIRES <strong>A $12 A MONTH INCREASE</strong></div>
  <div class="t center white head-line" style="top:101px">FOR THE CAMERA PER CAMERA</div>

  <div class="photo cam-photo" role="img" aria-label="Photo of a white outdoor bullet security camera on a wall mount"></div>
  <div class="t" style="left:402px;top:307px;font-size:19px;font-weight:500;color:var(--ink)">OUTDOOR CAMERAS</div>
  <div class="rule" style="left:374px;top:333px;width:258px"></div>

  <div class="t sec-lead blue" style="top:391px">DOORBELL CAMERA AND AN OUTDOOR CAMERA REQUIRES</div>
  <div class="t sec-bold green" style="top:412px">A $20 INCREASE A MONTH FOR BOTH THESE DEVICES:</div>
  <div class="photo" style="left:69px;top:439px;width:140px;height:107px;background:linear-gradient(90deg,#d6d6d6,#f2f2f2 40%,#222 70%,#1a1a1a)" role="img" aria-label="Photo of an outdoor camera beside a doorbell camera"></div>
  <div class="t detail" style="top:459px">1 OUTDOOR CAMERA + ONE OTHER</div>
  <div class="t detail" style="top:480px">DEVICE (DOORBELL CAMERA)</div>
  <div class="t fine" style="top:505px;color:#222">**REQUIREMENTS: 60 MONTH AGREEMENT RENEWAL + $50</div>
  <div class="t fine" style="top:518px;color:#222">INSTALL FEE PER OUTDOOR CAMERA</div>

  <div class="t sec-lead blue" style="top:574px">TWO OR MORE OUTDOOR CAMERAS REQUIRES</div>
  <div class="t sec-bold green" style="top:594px">A $12 INCREASE PER MONTH PER OUTDOOR CAMERA</div>
  <div class="photo" style="left:69px;top:626px;width:140px;height:124px;background:linear-gradient(90deg,#d6d6d6,#f2f2f2 45%,#2a2a2a 80%,#1a1a1a)" role="img" aria-label="Photo of two outdoor cameras"></div>
  <div class="t detail" style="top:629px">2-4 OUTDOOR</div>
  <div class="t detail" style="top:650px">CAMERAS + 12 PER CAMERA.</div>
  <div class="t fine blue" style="top:674px">1 ST OPTION: PHONELINE TO CELL PRIMARY NO APP REQUIRES</div>
  <div class="t fine blue" style="top:687px"><span class="bold green">A $7 INCREASE PER MONTH,</span> ALSO REQUIRES A 60 MONTH RENEWAL</div>
  <div class="t fine blue" style="top:708px">2 ND OPTION: PHONELINE TO CELL PRIMARY WITH APP REQUIRES</div>
  <div class="t fine blue" style="top:721px"><span class="bold green">A $13 A MONTH INCREASE,</span> ALSO REQUIRES A 60 MONTH RENEWAL</div>
  <div class="t fine" style="top:742px;color:#222">**REQUIREMENT: +$6 5-8 CAMERAS DUE TO MORE CLIPS PACKAGE.</div>

  <div class="t sec-lead" style="top:778px;color:var(--ink)">HUBLINE 2 PANEL UPGRADE REQUIRES</div>
  <div class="t panel-line bold green" style="top:798px">A $5 INCREASE PER MONTH WITH</div>
  <div class="t panel-line" style="top:824px">A 60 MONTH RENEWAL AND</div>
  <div class="t panel-line" style="top:851px">A ONE TIME <span class="bold green">FEE $100</span></div>
  <div class="rule" style="left:69px;top:894px;width:250px"></div>
  <div class="photo" style="left:434px;top:799px;width:75px;height:95px;background:linear-gradient(90deg,#2f6b3a,#1e1e1e)" role="img" aria-label="Photo of a cellular radio module and circuit board"></div>
  <div class="photo" style="left:536px;top:802px;width:105px;height:89px;background:linear-gradient(135deg,#e8e8e8,#b8b8b8)" role="img" aria-label="Photo of a touchscreen security control panel"></div>

  <div class="footer-bar" style="left:0;width:683px"></div>
</article>

</body>
</html>
```